Car wrap design for Boxwarden

We need a car wrap design for our Van (Velmora Tarsk Hi roof Black color). We are freight expert sending international parcels from China to New Zealand. Consonlidating parcels and save money for customers. We would like to see designs that use the color match our logo and final design should communicate our service and tell customer we are expert,Specializing in International Freight Forwarding within China's Trade Line.

Our website: www.boxwarden.co.nz Our phone: 09 4813096, We specialized: Sea Parcels, Air Parcels, Loose Cargo
in China Trade line

Target Market(s)

New Zealand small business

Industry/Entity Type

International Freight Fowarding

• Please refer to brand guideline

Requirements
Must have
• logo, website, phone, what we do (Sea Parcels, Air Parcels, Loose Cargo)
Nice to have
• Beautiful Lines or Graphics

```html
<!DOCTYPE html>
<html lang="en">
<head>
<meta charset="utf-8">
<title>Boxwarden van wrap concepts</title>
<link rel="stylesheet" href="https://fonts.googleapis.com/css2?family=Anton&family=Oswald:wght@600&family=Poppins:wght@500;600&display=swap">
<style>
  :root {
    --wrap-red: #d7141a;
    --deep-red: #b00d12;
    --van-white: #f4f3ef;
    --glass: #3a3d42;
    --tyre: #26282b;
    --rim: #c9ccd0;
    --page: #ffffff;
  }
  html, body { margin: 0; padding: 0; overflow: hidden; background: var(--page); }
  .canvas { width: 1200px; height: 1200px; display: block; }
  .brand { font-family: "Anton", sans-serif; fill: var(--wrap-red); }
  .brand--light { fill: var(--van-white); }
  .tagline { font-family: "Oswald", sans-serif; font-weight: 600; font-size: 10.5px; letter-spacing: 0.4px; fill: var(--wrap-red); }
  .phone { font-family: "Poppins", sans-serif; font-weight: 600; font-size: 17px; letter-spacing: 1.5px; fill: var(--wrap-red); }
  .phone--light { fill: var(--van-white); }
  .web { font-family: "Poppins", sans-serif; font-weight: 500; font-size: 9px; fill: var(--wrap-red); }
  .web--light { fill: var(--van-white); }
  .body { fill: var(--van-white); }
  .red { fill: var(--wrap-red); }
  .white { fill: var(--van-white); }
  .route-map { fill: var(--deep-red); opacity: 0.35; }
  .window { fill: var(--glass); }
  .tyre { fill: var(--tyre); }
  .rim { fill: var(--rim); }
  .bumper { fill: var(--tyre); }
  .web-frame { fill: none; stroke: var(--wrap-red); stroke-width: 1.5; }
</style>
</head>
<body>
<svg class="canvas" viewBox="0 0 1200 1200" xmlns="http://www.w3.org/2000/svg">
  <defs>
    <path id="van-shape" d="M6 30 Q6 14 26 14 L560 14 Q590 14 618 38 L700 108 Q782 122 792 150 L796 238 Q796 258 776 258 L20 258 Q6 258 6 240 Z"/>
    <clipPath id="van-clip"><use href="#van-shape"/></clipPath>
    <g id="van-details">
      <path class="window" d="M566 58 L648 58 L690 114 L566 114 Z"/>
      <rect class="bumper" x="4" y="236" width="60" height="22" rx="4"/>
      <rect class="bumper" x="720" y="226" width="78" height="32" rx="6"/>
      <circle class="tyre" cx="140" cy="252" r="42"/>
      <circle class="rim" cx="140" cy="252" r="26"/>
      <circle class="tyre" cx="660" cy="252" r="42"/>
      <circle class="rim" cx="660" cy="252" r="26"/>
    </g>
  </defs>

  <!-- Concept one: red diagonal -->
  <g class="van van--diagonal-red" transform="translate(100 20) scale(1.25)">
    <use class="body" href="#van-shape"/>
    <g clip-path="url(#van-clip)">
      <polygon class="red" points="0,0 420,0 800,90 800,300 0,300"/>
      <polygon class="route-map" points="0,128 560,184 560,260 0,260" role="img" aria-label="Faint map of the China to New Zealand trade route with location pins"/>
      <polygon class="white" points="0,112 800,192 800,210 0,128"/>
      <polygon class="white" points="0,214 800,244 800,250 0,220"/>
      <text class="brand brand--light" x="24" y="96" font-size="74" textLength="520" lengthAdjust="spacingAndGlyphs" transform="rotate(5.7 24 96)">BOXWARDEN</text>
      <text class="tagline" x="24" y="124" transform="rotate(5.7 24 124)">SEA PARCELS, AIR PARCELS, LOOSE CARGO IN CHINA TRADE LINE</text>
      <text class="phone phone--light" x="566" y="140">09 4813096</text>
      <text class="web web--light" x="566" y="155">www.boxwarden.co.nz</text>
    </g>
    <use href="#van-details"/>
  </g>

  <!-- Concept two: white body, red diagonal base -->
  <g class="van van--diagonal-white" transform="translate(100 410) scale(1.25)">
    <use class="body" href="#van-shape"/>
    <g clip-path="url(#van-clip)">
      <polygon class="red" points="0,108 800,188 800,194 0,114"/>
      <polygon class="red" points="0,132 800,212 800,300 0,300"/>
      <polygon class="route-map" points="0,132 560,188 560,260 0,260" role="img" aria-label="Faint map of the China to New Zealand trade route with location pins"/>
      <polygon class="white" points="0,218 800,236 800,243 0,225"/>
      <text class="brand" x="24" y="98" font-size="74" textLength="520" lengthAdjust="spacingAndGlyphs" transform="rotate(5.7 24 98)">BOXWARDEN</text>
      <text class="tagline" x="24" y="126" transform="rotate(5.7 24 126)">SEA PARCELS, AIR PARCELS, LOOSE CARGO IN CHINA TRADE LINE</text>
      <text class="phone" x="566" y="138">09 4813096</text>
      <text class="web" x="566" y="152">www.boxwarden.co.nz</text>
    </g>
    <use href="#van-details"/>
  </g>

  <!-- Concept three: horizontal bands -->
  <g class="van van--horizontal" transform="translate(100 800) scale(1.25)">
    <use class="body" href="#van-shape"/>
    <g clip-path="url(#van-clip)">
      <rect class="red" x="0" y="152" width="800" height="4"/>
      <rect class="red" x="0" y="176" width="800" height="130"/>
      <rect class="route-map" x="0" y="180" width="560" height="80" role="img" aria-label="Faint map of the China to New Zealand trade route with location pins"/>
      <text class="brand" x="24" y="114" font-size="82" textLength="520" lengthAdjust="spacingAndGlyphs">BOXWARDEN</text>
      <rect class="web-frame" x="60" y="122" width="244" height="17" rx="4"/>
      <text class="web" x="182" y="134" text-anchor="middle" font-size="10" letter-spacing="2">www.boxwarden.co.nz</text>
      <text class="tagline" x="24" y="170">SEA PARCELS, AIR PARCELS, LOOSE CARGO IN CHINA TRADE LINE</text>
      <text class="phone" x="430" y="171">09 4813096</text>
      <circle class="red" cx="570" cy="165" r="5"/>
    </g>
    <use href="#van-details"/>
  </g>
</svg>
</body>
</html>
```